redesing professional certificate

Redesign our certificate to more a professional look and to make it look like a-wanna have - Best in adobe photoshop, because this template will be our basic, and we have in our education different levels, basic, upper, lower, complex, master level. I usually add a small picture to show what level they are. Or when you have a better suggestion I a gladly to hear.
We teach to physiotherapist so it has to look professional.

Target Market(s)

physiotherapist

Industry/Entity Type

Health Care

Requirements
Must have
• our logo

```html
<!DOCTYPE html>
<html lang="en">
<head>
<meta charset="utf-8">
<title>Certificate – Myofa Institute</title>
<link rel="stylesheet" href="https://fonts.googleapis.com/css2?family=Montserrat:ital,wght@0,400;0,500;0,600;0,700;1,400&display=swap">
<style>
  :root {
    --navy: #1c2b3f;
    --yellow: #f8cc1b;
    --paper: #ffffff;
    --backdrop: #ece9e7;
    --text: #1f2d3f;
  }
  * { margin: 0; padding: 0; box-sizing: border-box; }
  html, body {
    width: 962px; height: 1200px; overflow: hidden;
    background: var(--backdrop);
    font-family: "Montserrat", Arial, sans-serif;
    color: var(--text);
  }
  .certificate {
    position: absolute; left: 31px; top: 282px;
    width: 900px; height: 636px;
    background: var(--paper);
    overflow: hidden;
    box-shadow: 0 4px 18px rgba(0,0,0,0.12);
  }
  .artwork { position: absolute; right: 0; top: 0; width: 900px; height: 636px; }
  .content {
    position: absolute; left: 0; top: 0; width: 604px; height: 636px;
    text-align: center;
  }
  .brand {
    position: absolute; top: 80px; left: 0; width: 100%;
    display: flex; justify-content: center; align-items: center; gap: 12px;
  }
  .brand-dot { width: 30px; height: 30px; border-radius: 50%; background: var(--navy); }
  .brand-name { font-weight: 700; font-size: 24px; color: var(--navy); letter-spacing: 0.5px; }
  .title {
    position: absolute; top: 188px; left: 0; width: 100%;
    font-weight: 600; font-size: 50px; letter-spacing: 2px; color: var(--navy);
  }
  .recipient-line {
    position: absolute; top: 296px; left: 64px; width: 478px;
    border-top: 1.5px solid var(--navy);
  }
  .course {
    position: absolute; top: 305px; left: 0; width: 100%;
    font-weight: 500; font-size: 15.5px; line-height: 19px;
  }
  .signatures {
    position: absolute; top: 460px; left: 0; width: 100%; height: 40px;
  }
  .signatory { position: absolute; width: 220px; text-align: center; }
  .signatory.left { left: 61px; }
  .signatory.right { left: 339px; }
  .signatory-name { font-weight: 600; font-size: 15px; }
  .signatory-role { font-style: italic; font-size: 13px; }
  .fine-print {
    position: absolute; top: 520px; left: 60px; width: 484px;
    font-size: 8.5px; line-height: 11px;
  }
  .fine-print p { margin-bottom: 9px; }
  .fine-print .tagline { font-style: italic; }
</style>
</head>
<body>
  <main class="certificate">
    <svg class="artwork" viewBox="0 0 900 636" role="img" aria-label="Illustration of a figure leaping up a staircase in yellow and navy">
      <defs>
        <linearGradient id="artworkTone" x1="0" y1="0" x2="0" y2="1">
          <stop offset="0" stop-color="#f8cc1b"/>
          <stop offset="0.65" stop-color="#f3c51a"/>
          <stop offset="1" stop-color="#1c2b3f"/>
        </linearGradient>
      </defs>
      <path d="M900 0 L900 636 L660 636 C720 520 640 420 610 320 C590 240 700 160 900 0 Z" fill="url(#artworkTone)"/>
    </svg>

    <section class="content">
      <div class="brand">
        <span class="brand-dot"></span>
        <span class="brand-name">Myofa Institute</span>
      </div>
      <h1 class="title">CERTIFICATE</h1>
      <div class="recipient-line"></div>
      <p class="course">
        has completed the FASCIATHERAPY LEVEL 1 course - 3 Days<br>
        15 - 17 February 2020<br>
        Kópavogur, Iceland 17 February 2020
      </p>
      <div class="signatures">
        <div class="signatory left">
          <div class="signatory-name">Mr. JT van Hal</div>
          <div class="signatory-role">Co-Director</div>
        </div>
        <div class="signatory right">
          <div class="signatory-name">Mr. RB Marsen</div>
          <div class="signatory-role">Co-Director</div>
        </div>
      </div>
      <div class="fine-print">
        <p>Registration number: 1 ICE 20</p>
        <p>The Myofa Institute ongoing certification is contingent upon meeting the requirements of the maintenance of the Certification of Fasciatherapy.</p>
        <p>Tissueline BV | Kanaalstraat 14, 1011AB Amsterdam, The Netherlands</p>
        <p class="tagline">Specialists in Fasciatherapy Innovation</p>
      </div>
    </section>
  </main>
</body>
</html>
```